Website Design: Business to Business Coaching/Strategy

DO NOT CONTACT ME PRIVATELY. ANY PRIVATE CONTACT WILL BE IGNORED.

I need a website design for a business to business coaching service.

The website is for a company the specializes in coaching/training for other businesses. The business specializes in business development and human resource management.

Where appropriate, please include calls to action, e.g.: book a service & request a quote

CONTENT (SEEE ATTACHMENT)
5 Pages;
1. Home Page with overview of company/services -> Slide show at the top with tagline:

WE HELP MAKE STRATEGY HAPPEN BY

DELIVERING LONG-TERM PERFORMANCE IMPROVEMENTS

SO COMPANIES CAN

"BECOME THE CHANGE THEY WISH TO SEE."

2. Works - core services; coaching; leadership development, workshops
3. Expertise
a. capability: helping people to help themselves
b. company interventions: working in partnership; team facilitation; …
c. testimonials
4. About Us
5. Inquires
a. business capability development and funding
b. Register / enrol for an open programme or workshop
c. client feedback

The website below provides services that are similar to the services of my company: https://www.velcormo.co.uk

DESIGN
- Dark theme matching this style of website BUT a simpler more straightforward design: https://www.duntalwick.ac.uk/
Another theme that I like - Dark themed with a modern/easy design: https://lorpaskins.com/theme-demos/?demo=glimvera-dark

Target Market(s)

Small businesses

Industry/Entity Type

Executive training/business coaching

Number of Pages Required

5+ page

Colors

Designer to choose colors to be used in the design.

```html
<!DOCTYPE html>
<html lang="en">
<head>
<meta charset="utf-8">
<title>Veloria — Business Coaching &amp; Strategy</title>
<link href="https://fonts.googleapis.com/css2?family=Michroma&family=Lato:wght@400;700&display=swap" rel="stylesheet">
<style>
:root{
  --bg:#000;
  --panel:#1a1a1a;
  --tile-dark:#1c1c1c;
  --blue:#1a8fe3;
  --orange:#e8401c;
  --white:#fff;
  --text:#cfcfcf;
  --muted:#9a9a9a;
  --line:#333;
}
*{margin:0;padding:0;box-sizing:border-box}
html,body{width:1200px;height:4335px;overflow:hidden;background:var(--bg)}
body{position:relative;font-family:"Lato",sans-serif;color:var(--white)}
.abs{position:absolute}
.display{font-family:"Michroma",sans-serif;text-transform:uppercase;letter-spacing:1px}
p{font-size:13px;line-height:18.5px;color:var(--text)}

/* header */
.site-header{position:absolute;left:0;top:0;width:1200px;height:86px;background:var(--bg)}
.brand{left:130px;top:28px;font-size:24px;font-family:"Michroma",sans-serif;letter-spacing:2px;text-transform:uppercase}
.nav a{position:absolute;top:34px;font-size:13px;color:var(--white);text-decoration:none;letter-spacing:.5px}
.nav a.active{color:var(--blue)}
.nav a.active::after{content:"";position:absolute;left:0;right:0;top:21px;height:2px;background:var(--blue)}
.header-phone{left:925px;top:28px;display:flex;align-items:center;gap:8px;font-size:14px;color:#ddd}

/* hero */
.hero{left:0;top:86px;width:1200px;height:589px;background:linear-gradient(160deg,#6d6660 0%,#4a3e36 40%,#2c2824 70%,#3b332c 100%)}
.hero-title{left:200px;top:118px;width:800px;text-align:center;font-size:24px;line-height:27px;color:var(--white)}
.btn{position:absolute;display:flex;align-items:center;justify-content:center;font-family:"Michroma",sans-serif;text-transform:uppercase;font-size:13px;letter-spacing:1px;color:var(--white)}
.btn-blue{background:var(--blue)}
.btn-orange{background:var(--orange)}
.dots{left:560px;top:631px;display:flex;gap:8px;align-items:center}
.dots span{width:6px;height:6px;border-radius:50%;background:#fff}
.dots span.on{width:11px;height:11px;background:var(--blue);border:2px solid #fff}

/* services */
.section-title{width:1200px;left:0;text-align:center;font-size:21px}
.rule{height:3px;background:var(--blue)}
.photo{position:absolute}
.service-title{font-size:17px}
.service-text{width:440px}

/* personalised */
.approach{left:532px;top:1883px;width:537px;height:270px;background:var(--blue);padding:64px 42px 0}
.approach h3{font-size:21px;font-weight:400;margin-bottom:26px}
.approach p{font-size:16px;line-height:23px;color:var(--white)}

/* works tiles */
.tile{position:absolute;background:var(--orange);display:flex;flex-direction:column;align-items:center;justify-content:center;gap:22px}
.tile span{font-family:"Michroma",sans-serif;text-transform:uppercase;font-size:15px;letter-spacing:1px;text-align:center;line-height:25px}

/* expertise */
.exp-box{position:absolute;top:2989px;width:167px;height:167px;background:var(--tile-dark);display:flex;flex-direction:column;align-items:center;justify-content:center;gap:18px}
.exp-box span{font-family:"Michroma",sans-serif;text-transform:uppercase;font-size:11px;text-align:center;line-height:17px}

/* about + multi */
.about{left:0;top:3236px;width:1200px;height:391px;background:var(--panel)}
.multi{left:0;top:3627px;width:1200px;height:363px;background:var(--panel)}

/* footer */
.site-footer{left:0;top:3990px;width:1200px;height:345px;background:var(--bg)}
.foot-h{font-size:12px;font-weight:700;letter-spacing:1px}
.foot-list a{display:block;font-size:12px;color:#ddd;text-decoration:none;line-height:20px}
.foot-item{display:flex;gap:14px;align-items:center;font-size:12px;color:#ddd;line-height:16px;position:absolute}
.foot-icon{width:22px;height:22px;border-radius:50%;background:#fff;display:flex;align-items:center;justify-content:center;flex:none}
.copyright{left:0;top:4288px;width:1200px;text-align:center;font-size:11px;color:#ccc}
</style>
</head>
<body>

<header class="site-header">
  <div class="abs brand">Veloria</div>
  <nav class="nav">
    <a class="active" style="left:428px">HOME</a>
    <a style="left:512px">WORKS</a>
    <a style="left:607px">EXPERTISE</a>
    <a style="left:719px">ABOUT US</a>
    <a style="left:823px">INQUIRES</a>
  </nav>
  <div class="abs header-phone">
    <svg width="26" height="26" viewBox="0 0 24 24" fill="none" stroke="#ddd" stroke-width="1.5"><path d="M5 3h4l2 5-3 2a12 12 0 0 0 6 6l2-3 5 2v4a2 2 0 0 1-2 2A17 17 0 0 1 3 5a2 2 0 0 1 2-2z"/></svg>
    555.014.2290
  </div>
</header>

<section class="abs hero" role="img" aria-label="Photo of a presenter at a flip chart leading a meeting with a seated team in a bright office"></section>
<h1 class="abs hero-title display" style="font-weight:400">We help make strategy happen by delivering long-term performance improvements so companies can "Become the change they wish to see."</h1>
<a class="btn btn-blue" style="left:379px;top:251px;width:203px;height:54px">Book a Service</a>
<a class="btn btn-orange" style="left:597px;top:251px;width:224px;height:54px">Request a Quote</a>
<div class="abs dots"><span></span><span></span><span class="on"></span><span></span><span></span></div>

<!-- services -->
<h2 class="abs section-title display" style="top:725px;font-weight:400">Our Services</h2>
<div class="abs rule" style="left:580px;top:768px;width:39px"></div>

<div class="photo" style="left:130px;top:823px;width:451px;height:240px;background:linear-gradient(180deg,#cfd3d6,#6b6f72 60%,#2d2f31)" role="img" aria-label="Photo of a team meeting around a table in a glass-walled boardroom"></div>
<div class="photo" style="left:619px;top:823px;width:451px;height:240px;background:linear-gradient(135deg,#1e2124,#3a3836 60%,#6a5a44)" role="img" aria-label="Photo of hands typing on a laptop with assessment chalk sketches"></div>
<h3 class="abs service-title display" style="left:130px;top:1094px;font-weight:400">Leadership &amp; Capability</h3>
<h3 class="abs service-title display" style="left:619px;top:1094px;font-weight:400">Assessment &amp; Analysis</h3>
<p class="abs service-text" style="left:130px;top:1130px">There is a pressing need for leadership to be distributed across organisations in support of constant innovation and change. For businesses that believe there is a benefit in investing in their core resource – people, we can help you gain a clear return on investment, improve profitability, build your leadership capacity and contribute to creating a high-performing organisation.</p>
<p class="abs service-text" style="left:619px;top:1130px">We engage key stakeholders to identify issues, clarify direction and to have conversations about those areas that really matter. We help clients to commit to action, implement new business strategies, plan for the future and achieve business growth. Our personalised coaching enables us to put an objective lens on the goals you wish to achieve.</p>

<div class="photo" style="left:130px;top:1284px;width:451px;height:241px;background:linear-gradient(180deg,#7b7f7d,#c8c6c0 45%,#8a8d8e)" role="img" aria-label="Photo of a cheerful team giving a group high five"></div>
<div class="photo" style="left:619px;top:1284px;width:451px;height:241px;background:linear-gradient(135deg,#d8dee2,#b7c2c9 50%,#eef1f3)" role="img" aria-label="Photo of hands reviewing charts on paper with a pen"></div>
<h3 class="abs service-title display" style="left:130px;top:1556px;font-weight:400">People &amp; Engagement</h3>
<h3 class="abs service-title display" style="left:622px;top:1556px;font-weight:400">Investigate &amp; Guide</h3>
<p class="abs service-text" style="left:130px;top:1592px">It's all about people; that is, the right people. Having leaders with an ability to facilitate the fulfilment of your company's purpose through your people provides potential for it to become a great organisation. Dealing with change is dealing with peoples emotions. We are interested in improvement, not change. Specifically, we are keen on developing companies and leaders who want to create a great organisation and are willing to lead a process that engages stakeholders in its quest for continuous improvement and long-term viability.</p>
<p class="abs service-text" style="left:622px;top:1592px">Success in bussiness hinges on strategic agility as well as an ability to highlight and execute actions leading to measurable improvements. To help businesses to do this we will support, guide and partner with clients to assess, plan for and strengthen their capability through the design of strategies to overcome barriers and produce measurable impact. Our experience in consultancy and company intervention will provide an objective focus to uncover unknown factors and develop an actionable plan for you to execute.</p>

<!-- personalised approach -->
<div class="photo" style="left:130px;top:1840px;width:402px;height:346px;background:linear-gradient(120deg,#3a4652,#6d7d8a 50%,#a9c3da)" role="img" aria-label="Photo of two smiling businessmen shaking hands"></div>
<div class="abs approach">
  <h3 class="display">A Personalised Approach</h3>
  <p>Working in partnership we will learn about your business and your challenges for the purpose of designing a programme appropriate to your situation.</p>
</div>

<!-- works -->
<h2 class="abs section-title display" style="top:2262px;font-weight:400">Works</h2>

<div class="tile" style="left:130px;top:2328px;width:299px;height:215px">
  <svg width="76" height="72" viewBox="0 0 76 72" fill="none" stroke="#fff" stroke-width="2"><circle cx="38" cy="12" r="7"/><circle cx="16" cy="20" r="6"/><circle cx="60" cy="20" r="6"/><path d="M26 70V34a6 6 0 0 1 6-6h12a6 6 0 0 1 6 6v36M38 48v22M6 70V38a5 5 0 0 1 5-5h10M70 70V38a5 5 0 0 0-5-5H55M16 50v20M60 50v20"/></svg>
  <span>People &amp; Change</span>
</div>
<div class="tile" style="left:449px;top:2328px;width:300px;height:451px">
  <svg width="76" height="72" viewBox="0 0 76 72" fill="none" stroke="#fff" stroke-width="2"><circle cx="38" cy="12" r="9"/><circle cx="14" cy="56" r="9"/><circle cx="62" cy="56" r="9"/><path d="M31 19 19 48M45 19l12 29M23 56h30"/><circle cx="38" cy="40" r="5"/></svg>
  <span>Organisation<br>Performance</span>
</div>
<div class="tile" style="left:771px;top:2328px;width:299px;height:215px">
  <svg width="76" height="76" viewBox="0 0 76 76" fill="none" stroke="#fff" stroke-width="2"><circle cx="38" cy="38" r="34"/><circle cx="38" cy="38" r="22"/><path d="M24 30c6 0 8 4 12 4s4 6 0 8-2 10-6 10M44 20c0 6 6 6 6 12s8 2 8 8"/></svg>
  <span>Sustainability</span>
</div>
<div class="tile" style="left:130px;top:2565px;width:299px;height:214px">
  <svg width="76" height="72" viewBox="0 0 76 72" fill="none" stroke="#fff" stroke-width="2"><path d="M6 22h14a6 6 0 1 1 12 0h12v12a6 6 0 1 0 0 12v14H32a6 6 0 1 0-12 0H6V46a6 6 0 1 1 0-12z"/><path d="M52 6l14 6-4 8a5 5 0 1 1-6 6l-4 8-12-6"/></svg>
  <span>Strategy &amp; Direction</span>
</div>
<div class="tile" style="left:771px;top:2565px;width:299px;height:214px">
  <svg width="76" height="76" viewBox="0 0 76 76" fill="none" stroke="#fff" stroke-width="2"><circle cx="38" cy="38" r="34"/><circle cx="38" cy="38" r="9"/><path d="M38 18v6M38 52v6M18 38h6M52 38h6M24 24l4 4M48 48l4 4M52 24l-4 4M24 52l4-4"/><circle cx="38" cy="38" r="17"/></svg>
  <span>Operations &amp; Risk</span>
</div>

<!-- expertise -->
<h2 class="abs display" style="left:133px;top:2862px;font-size:24px;font-weight:400">Expertise</h2>
<p class="abs" style="left:133px;top:2925px;width:350px">Sed ut perspiciatis unde omnis iste natus error sit voluptatem accusantium doloremque laudantium, totam rem aperiam, eaque ipsa quae ab illo inventore veritatis et quasi architecto beatae vitae dicta sunt explicabo. Nemo enim ipsam voluptatem quia voluptas sit aspernatur aut odit aut fugit, sed quia consequuntur magni dolores eos qui ratione voluptatem sequi nesciunt. Neque porro quisquam.</p>
<a class="btn btn-blue" style="left:131px;top:3102px;width:138px;height:55px;font-family:Lato,sans-serif;font-weight:700;font-size:15px">REGISTER</a>
<a class="btn btn-orange" style="left:284px;top:3102px;width:159px;height:55px;font-family:Lato,sans-serif;font-weight:700;font-size:15px">CONTACT US</a>

<h2 class="abs display" style="left:590px;top:2860px;width:466px;text-align:center;font-size:19px;line-height:31px;font-weight:400">For leaders who believe focused development presents a competitive edge.</h2>
<div class="exp-box" style="left:542px">
  <svg width="52" height="50" viewBox="0 0 52 50" fill="none" stroke="#fff" stroke-width="1.8"><rect x="8" y="3" width="40" height="26"/><path d="M14 22l8-8 6 5 12-10"/><circle cx="8" cy="34" r="4"/><path d="M2 48v-6a6 6 0 0 1 12 0v6M20 48v-4h28v4"/><circle cx="26" cy="38" r="3"/><circle cx="36" cy="38" r="3"/><circle cx="46" cy="38" r="3"/></svg>
  <span>Coaching &amp;<br>Mentoring</span>
</div>
<div class="exp-box" style="left:722px">
  <svg width="52" height="52" viewBox="0 0 52 52" fill="none" stroke="#fff" stroke-width="1.8"><circle cx="26" cy="26" r="8"/><circle cx="26" cy="5" r="4"/><circle cx="26" cy="47" r="4"/><circle cx="5" cy="26" r="4"/><circle cx="47" cy="26" r="4"/><circle cx="10" cy="10" r="3"/><circle cx="42" cy="42" r="3"/><circle cx="42" cy="10" r="3"/><circle cx="10" cy="42" r="3"/><path d="M26 9v9M26 34v9M9 26h9M34 26h9"/></svg>
  <span>Leadership</span>
</div>
<div class="exp-box" style="left:902px">
  <svg width="52" height="50" viewBox="0 0 52 50" fill="none" stroke="#fff" stroke-width="1.8"><circle cx="26" cy="8" r="4"/><circle cx="16" cy="12" r="3"/><circle cx="36" cy="12" r="3"/><path d="M18 28v-6a8 8 0 0 1 16 0v6M4 20l8 16 8 4v8M48 20l-8 16-8 4v8"/></svg>
  <span>Training &amp;<br>Development</span>
</div>

<!-- about -->
<section class="abs about">
  <div class="abs" style="left:0;top:0;width:606px;height:391px;background:linear-gradient(90deg,#2a3038,#59636d 45%,#3a3f44 80%,#1a1a1a)" role="img" aria-label="Photo of business people in suits shaking hands in an office"></div>
  <h2 class="abs display" style="left:631px;top:55px;font-size:22px;font-weight:400">About Us</h2>
  <h3 class="abs display" style="left:631px;top:95px;font-size:19px;line-height:28px;font-weight:400;color:#ddd;text-transform:none">Helping Businesses Achieve<br>Transformational Change</h3>
  <p class="abs" style="left:631px;top:168px;width:420px;color:#bbb">Transformation is incredibly hard and like many businesses, we too have had to be adaptive and learn to become agile in how we engage organisations and add value in a sustainable way.</p>
  <p class="abs" style="left:631px;top:245px;width:420px;color:#bbb">Having a strong desire to make a difference, we help business owners who want to deal with pressing change affecting themselves and their business. We are committed to supporting less well off organisations and charities, through discretionary pricing on programmes and Community Mentoring engagements.</p>
</section>

<!-- multi-disciplined -->
<section class="abs multi">
  <div class="abs" style="left:606px;top:0;width:594px;height:363px;background:linear-gradient(90deg,#1a1a1a,#4d5863 30%,#8b98a4 65%,#c8d2da)" role="img" aria-label="Photo of a presenter leading a workshop with colleagues around a glass table"></div>
  <h2 class="abs display" style="left:133px;top:72px;font-size:21px;line-height:32px;font-weight:400">Multi-Disciplined<br>Personally Committed<br>to Making a Difference</h2>
  <p class="abs" style="left:133px;top:183px;width:425px;color:#bbb">We apply consultancy &amp; company intervention at an individual and company level with a focus of enhancing business practices. These range from hands on one-on-one coaching for business owners and their managers, to delivering interactive programmes across several months. All our engagements are designed to improve leadership, reduce staff issues and sustain business performance by establishing business strategy and executing actions against priorities.</p>
</section>

<!-- footer -->
<footer class="abs site-footer">
  <div class="abs brand" style="left:165px;top:114px;font-size:28px;top:122px">Veloria</div>

  <div class="abs foot-h" style="left:475px;top:48px">MENU</div>
  <div class="abs foot-list" style="left:475px;top:81px">
    <a>HOME</a><a>WORKS</a><a>EXPERTISE</a><a>ABOUT US</a><a>INQUIRES</a>
  </div>

  <div class="abs foot-h" style="left:665px;top:48px">CONTACT US</div>
  <div class="foot-item" style="left:665px;top:82px">
    <span class="foot-icon"><svg width="12" height="12" viewBox="0 0 12 12"><path d="M6 0a4 4 0 0 1 4 4c0 3-4 8-4 8S2 7 2 4a4 4 0 0 1 4-4z" fill="#000"/><circle cx="6" cy="4" r="1.5" fill="#fff"/></svg></span>
    <span>2716 Harlow Street<br>Brenmoor, CA 90412</span>
  </div>
  <div class="foot-item" style="left:665px;top:132px">
    <span class="foot-icon"><svg width="12" height="12" viewBox="0 0 24 24"><path d="M5 3h4l2 5-3 2a12 12 0 0 0 6 6l2-3 5 2v4a2 2 0 0 1-2 2A17 17 0 0 1 3 5a2 2 0 0 1 2-2z" fill="#000"/></svg></span>
    <span>Call Us<br>555.014.2290</span>
  </div>
  <div class="foot-item" style="left:665px;top:183px">
    <span class="foot-icon"><svg width="12" height="10" viewBox="0 0 12 10"><rect x="0" y="0" width="12" height="10" fill="#000"/><path d="M0 0l6 5 6-5" stroke="#fff" fill="none"/></svg></span>
    <span>E mail Us<br>hello@veloria-coaching.com</span>
  </div>

  <div class="abs foot-h" style="left:956px;top:48px">FOLLOW US</div>
  <div class="foot-item" style="left:956px;top:82px"><span class="foot-icon"></span><span>Like us on<br>FRIENDLANE</span></div>
  <div class="foot-item" style="left:956px;top:132px"><span class="foot-icon"></span><span>Follow us on<br>CHIRPWIRE</span></div>
  <div class="foot-item" style="left:956px;top:183px"><span class="foot-icon"></span><span>Follow us on<br>LINKWORK</span></div>

  <div class="abs" style="left:130px;top:265px;width:940px;height:1px;background:var(--line)"></div>
</footer>
<div class="abs copyright">Copyright © 2022 All Rights Reserved</div>

</body>
</html>
```